Company Mission & Values Poster

I'd like an A2 Portrait Poster displaying our company's Mission & Values.
See our website for our logo, fonts, mission & values.
https://valtemo.com.au/

Our Mission: Creating homes for abundant life
Values: Love, Thinking, Team, Zoe.

Some ideas to consider:
Mission as the Headline then
A logo for each of the 4 Values and the words

Target Market(s)

Myself & my team

Industry/Entity Type

Real Estate

Font styles to use
Other font styles liked:
• Company fonts as seen on our website

```html
<!DOCTYPE html>
<html lang="en">
<head>
<meta charset="utf-8">
<title>Valtemo — Mission &amp; Values Poster</title>
<link rel="stylesheet" href="https://fonts.googleapis.com/css2?family=Source+Serif+4:opsz,wght@8..60,500;8..60,600&display=swap">
<style>
  :root {
    --ink: #0f3a2d;
    --paper: #ffffff;
    --backdrop: #f4f4f3;
    --haze: #f1f3f3;
    --sea-light: #d3dcdd;
    --sea-deep: #9fb2b8;
    --sand: #c8a47c;
    --wall: #4a443d;
    --logo-text: #ffffff;
  }
  * { box-sizing: border-box; margin: 0; padding: 0; }
  html, body {
    width: 1200px; height: 1200px; overflow: hidden;
    background: var(--backdrop);
  }
  .poster {
    position: absolute; left: 180px; top: 0;
    width: 840px; height: 1200px;
    background: var(--paper);
    overflow: hidden;
    font-family: "Source Serif 4", Georgia, serif;
    color: var(--ink);
  }
  .beach-photo {
    position: absolute; left: 0; right: 0; top: 470px; bottom: 0;
    background: linear-gradient(to bottom,
      rgba(255,255,255,1) 0%,
      var(--haze) 10%,
      var(--sea-light) 30%,
      var(--sea-deep) 62%,
      #b7b3a4 72%,
      var(--sand) 82%,
      #9c8064 90%,
      var(--wall) 100%);
  }
  .eyebrow {
    position: absolute; top: 80px; width: 100%;
    text-align: center; font-size: 38px; font-weight: 500; line-height: 1;
  }
  .rule {
    position: absolute; left: 87px; width: 657px; height: 6px; display: block;
  }
  .rule-top { top: 140px; }
  .rule-bottom { top: 303px; }
  .headline {
    position: absolute; top: 156px; width: 100%;
    text-align: center; font-size: 58px; font-weight: 600; line-height: 70px;
    letter-spacing: -0.3px;
  }
  .values { position: absolute; top: 0; left: 0; width: 100%; list-style: none; }
  .value {
    position: absolute; width: 100%; text-align: center;
    font-size: 54px; font-weight: 600; line-height: 1;
  }
  .value-dot {
    display: block; margin: 0 auto 14px;
    width: 26px; height: 26px; border: 2px solid var(--ink); border-radius: 50%;
  }
  .brand {
    position: absolute; left: 514px; top: 1138px;
    display: flex; align-items: center; gap: 14px;
    color: var(--logo-text);
    font-size: 34px; font-weight: 500; letter-spacing: 5px; line-height: 1;
  }
  .brand-dot {
    width: 30px; height: 30px; border: 2px solid var(--logo-text); border-radius: 50%;
  }
</style>
</head>
<body>
  <main class="poster">
    <div class="beach-photo" role="img" aria-label="Sunny harbour beach with moored yachts, swimmers in calm water and a couple relaxing on the sand beneath a red beach umbrella"></div>

    <p class="eyebrow">Our Mission:</p>
    <svg class="rule rule-top" viewBox="0 0 657 6" preserveAspectRatio="none" aria-hidden="true">
      <path d="M0 3 Q328 -1 657 3 Q328 7 0 3 Z" fill="var(--ink)"/>
    </svg>
    <h1 class="headline">Creating homes for<br>abundant life</h1>
    <svg class="rule rule-bottom" viewBox="0 0 657 6" preserveAspectRatio="none" aria-hidden="true">
      <path d="M0 3 Q328 -1 657 3 Q328 7 0 3 Z" fill="var(--ink)"/>
    </svg>

    <ul class="values">
      <li class="value" style="top:356px"><span class="value-dot"></span>Love</li>
      <li class="value" style="top:485px"><span class="value-dot"></span>Thinking</li>
      <li class="value" style="top:614px"><span class="value-dot"></span>Team</li>
      <li class="value" style="top:743px"><span class="value-dot"></span>Zoe</li>
    </ul>

    <div class="brand"><span class="brand-dot"></span>VALTEMO</div>
  </main>
</body>
</html>
```